Flyer-Design für Hausarztpraxis
Zielgruppe
Hausarztpraxis, Zielgruppe junge Patienten ...
Aufgabenstellung
Mein aktueller Flyer sollte modernisiert werden ... Texte können gern überarbeitet werden... Neue Fotos der Praxis werden noch gemacht. DH die Datei sollte so sein, dass ich die Fotos anpassen kann hinterher
Farbe gern in dem schönen Magenta wie das Logo
Aufbau des Flysers sollte ebenfalls optimiert werden.

```html
<!DOCTYPE html>
<html lang="de">
<head>
<meta charset="utf-8">
<title>Hausarztpraxis Flyer – Innenseite</title>
<link href="https://fonts.googleapis.com/css2?family=Open+Sans:wght@400;600;700;800&display=swap" rel="stylesheet">
<style>
  :root {
    --magenta: #d4264f;
    --magenta-deep: #b81f2c;
    --red-band: #c82232;
    --ink: #3a3a3a;
    --muted: #6b6b6b;
    --paper: #ffffff;
    --paper-warm: #efedeb;
    --grey-soft: #d9dadc;
    --stage: #e4e0dc;
  }
  * { box-sizing: border-box; margin: 0; padding: 0; }
  html, body { width: 1200px; height: 960px; overflow: hidden; }
  body {
    background: var(--stage);
    font-family: "Open Sans", Arial, sans-serif;
    color: var(--ink);
    position: relative;
  }
  .flyer {
    position: absolute;
    left: 45px; top: 88px;
    width: 1110px; height: 785px;
    display: flex;
    background: var(--paper);
    box-shadow: 0 10px 30px rgba(0,0,0,.12);
  }
  .panel { position: relative; width: 370px; height: 100%; overflow: hidden; }

  /* Panel 1: Leistungen */
  .services { background: var(--paper); }
  .services__frame {
    position: absolute; left: 0; top: 26px; right: 26px; bottom: 26px;
    border-top: 1.5px solid var(--magenta);
    border-right: 1.5px solid var(--magenta);
    border-bottom: 1.5px solid var(--magenta);
    z-index: 3; pointer-events: none;
  }
  .services__title {
    position: absolute; left: 30px; top: 40px; right: 40px;
    color: var(--magenta); font-weight: 700; font-size: 19px;
    letter-spacing: .2px; text-transform: uppercase; z-index: 2;
  }
  .services__list {
    position: absolute; left: 42px; top: 84px; right: 44px;
    list-style: none; font-size: 12.5px; line-height: 1.42; color: var(--muted); z-index: 2;
  }
  .services__list li::before { content: "- "; }
  .extras {
    position: absolute; left: 0; right: 0; bottom: 0; height: 390px;
    background: linear-gradient(180deg, #e6e7e9 0%, #cfd1d4 100%);
  }
  .extras__wave { position: absolute; left: 0; top: -30px; width: 100%; height: 60px; }
  .extras__title {
    position: absolute; left: 30px; top: 26px; right: 40px;
    color: var(--magenta); font-weight: 700; font-size: 15.5px; line-height: 1.25; z-index: 2;
  }
  .extras__list {
    position: absolute; left: 42px; top: 74px; right: 44px;
    list-style: none; font-size: 12px; line-height: 1.42; color: #fff; z-index: 2;
  }
  .extras__list li::before { content: "- "; }
  .extras__photo {
    position: absolute; left: 0; bottom: 0; width: 100%; height: 190px;
    background: linear-gradient(160deg, rgba(255,255,255,0) 10%, #b9c0c8 55%, #8fa3b8 100%);
  }

  /* Panel 2: Telefonnummern */
  .contacts { background: var(--paper); }
  .contacts__edge { position: absolute; left: 0; top: 0; width: 100%; height: 8px; background: var(--magenta); z-index: 2; }
  .contacts__photo {
    position: absolute; left: 0; top: 0; width: 100%; height: 420px;
    background: linear-gradient(180deg, #a9cfe0 0%, #dfe9ee 42%, #9a9896 62%, #6f6c6a 100%);
  }
  .contacts__title {
    position: absolute; left: 28px; top: 452px; right: 20px;
    color: var(--magenta); font-weight: 800; font-size: 19px; text-transform: uppercase; letter-spacing: -.2px;
  }
  .phone-table { position: absolute; left: 40px; top: 500px; width: 300px; border-collapse: collapse; font-size: 13.5px; }
  .phone-table td { padding: 3px 0; color: var(--ink); }
  .phone-table td:last-child { text-align: right; padding-left: 12px; }

  /* Panel 3: Titelseite */
  .cover { background: var(--paper-warm); }
  .cover__shapes { position: absolute; inset: 0; width: 100%; height: 100%; }
  .brand {
    position: absolute; left: 20px; right: 20px; top: 58px; text-align: center; z-index: 2;
  }
  .brand__dot { display: block; margin: 0 auto 10px; width: 38px; height: 38px; border-radius: 50%; background: var(--magenta); }
  .brand__name { color: var(--magenta); font-weight: 600; font-size: 19px; line-height: 1.25; }
  .brand__rule { height: 1px; background: #8b8b8b; margin: 8px 18px 5px; }
  .brand__tagline { font-size: 9px; letter-spacing: 2px; text-transform: uppercase; color: var(--muted); }
  .cover__info {
    position: absolute; left: 28px; right: 20px; top: 598px; color: #fff; z-index: 2;
    font-size: 12.5px; line-height: 1.35;
  }
  .cover__doctor { font-weight: 800; font-size: 16.5px; text-transform: uppercase; margin-bottom: 2px; }
  .cover__hours-title { font-weight: 800; text-decoration: underline; margin-top: 8px; text-transform: uppercase; }
</style>
</head>
<body>
  <main class="flyer">
    <section class="panel services">
      <div class="services__frame"></div>
      <h2 class="services__title">Unser Leistungsspektrum</h2>
      <ul class="services__list">
        <li>Vollständige hausärztliche Versorgung</li>
        <li>Gesundheitsvorsorge</li>
        <li>Krebsvorsorge</li>
        <li>EKG und Ergometrie</li>
        <li>Sonographie Bauch, Schilddrüse, Gefäße</li>
        <li>Langzeitblutdruckmessung</li>
        <li>Lungenfunktionsprüfung</li>
        <li>Laboruntersuchungen</li>
        <li>Sämtliche Impfungen</li>
        <li>Kleine operative Eingriffe</li>
        <li>Wundversorgung</li>
        <li>Autogenes Training</li>
        <li>Neuraltherapie</li>
      </ul>
      <div class="extras">
        <svg class="extras__wave" viewBox="0 0 370 60" preserveAspectRatio="none" aria-hidden="true">
          <path d="M0 30 Q185 0 370 34 L370 60 L0 60 Z" fill="#e6e7e9"/>
        </svg>
        <div class="extras__photo" role="img" aria-label="Foto: Hände beim Anziehen blauer Einmalhandschuhe"></div>
        <h3 class="extras__title">Zusätzliche individuelle<br>Gesundheitsleistungen</h3>
        <ul class="extras__list">
          <li>Ästhetische Anwendungen mittels Hyaluronsäurefiller im Gesicht</li>
          <li>Infusionsbehandlungen</li>
          <li>Depressionstherapie</li>
          <li>Vitaminaufbaukuren</li>
          <li>Sportuntersuchungen</li>
          <li>Patientenverfügungen</li>
        </ul>
      </div>
    </section>

    <section class="panel contacts">
      <div class="contacts__edge"></div>
      <div class="contacts__photo" role="img" aria-label="Foto: Marktplatz mit Fachwerkhäusern unter blauem Himmel"></div>
      <h2 class="contacts__title">Nützliche Telefonnummern</h2>
      <table class="phone-table">
        <tr><td>Praxis Dr. Hohenstein</td><td>4815</td></tr>
        <tr><td>Rettungsdienst</td><td>112</td></tr>
        <tr><td>Ärztlicher Bereitschaftsdienst</td><td>116117</td></tr>
        <tr><td>Linden-Apotheke Talheim</td><td>27504</td></tr>
        <tr><td>Polizei/ Notruf</td><td>110</td></tr>
        <tr><td>Giftnotruf</td><td>0761/1234567</td></tr>
        <tr><td>Kreisklinik Talheim</td><td>250</td></tr>
      </table>
    </section>

    <section class="panel cover">
      <svg class="cover__shapes" viewBox="0 0 370 785" preserveAspectRatio="none">
        <defs>
          <linearGradient id="doctorTone" x1="0" y1="0" x2="1" y2="1">
            <stop offset="0" stop-color="#e9edf1"/>
            <stop offset=".55" stop-color="#b9c2cb"/>
            <stop offset="1" stop-color="#3b3d42"/>
          </linearGradient>
          <linearGradient id="bandTone" x1="0" y1="0" x2="1" y2="0">
            <stop offset="0" stop-color="#c21f2e"/>
            <stop offset="1" stop-color="#d4264f"/>
          </linearGradient>
        </defs>
        <rect x="0" y="0" width="370" height="10" fill="#d4264f"/>
        <path d="M0 270 L370 200 L370 600 L0 600 Z" fill="url(#doctorTone)" role="img" aria-label="Foto: Ärztin im weißen Kittel mit Stethoskop"/>
        <path d="M0 584 L370 540 L370 785 L0 785 Z" fill="url(#bandTone)"/>
      </svg>
      <div class="brand">
        <span class="brand__dot"></span>
        <div class="brand__name">Hausarztpraxis<br>Dr. med. Marlene Hohenstein</div>
        <div class="brand__rule"></div>
        <div class="brand__tagline">Weil wir lieben, was wir machen</div>
      </div>
      <div class="cover__info">
        <div class="cover__doctor">Dr. med. Marlene Hohenstein</div>
        <div>Fachärztin f. Allgemeinmedizin</div>
        <div>Lindenweg 14 - 71234 Talheim</div>
        <div class="cover__hours-title">Sprechzeiten</div>
        <div>MO 8-11:30 sowie 14-17 Uhr</div>
        <div>DI/ MI 8-13 Uhr</div>
        <div>DO 8-11:30 sowie 14-18 Uhr</div>
        <div>FR 8-11:30</div>
      </div>
    </section>
  </main>
</body>
</html>
```